・メインで紹介していただく2つのアクティビティーの情報は
以下のHPアドレスにございます。
https://kurumi-lodge.example.jp/wp/activities/星あかりの小径/
https://kurumi-lodge.example.jp/wp/activities/ムーンライトトレック/

・写真素材はグーグルのマイドライブ↓に格納いたしました
https://files.example.net/open?id=8XqPzLmTr2WvNc4Ka7bYdE1hJsG9uFoRt

・写真素材についてはトリミングも含め自由にお使いいただけます。デザインによっては数枚省いていただいても結構です。
~写真の説明~
1「山岳学舎を取り巻く山々」×2のどちらか :山岳学舎施設が山の中にあるというイメージを前面に押し出して頂きたい。
2「山岳学舎紹介・・・・」の写真は施設情報のところで小さくお使いください
そのなかでも「スカイランタン」と「スノースライダー」は こんなこともや
っているよ!程度の小さな丸切り抜きで添えてもらえれば結構です。

・納期期限:10月4日厳守でお願いします。作成過程で、連絡を取りながら作成していただける方を優先させていただきたいと存じます。
【星あかりの小径】
■催行期間 2019年 12月 14日(土)~2020年 4月5日(日) 一日3回
■料  金 小学生以上2,000円(スノーシューレンタル料込)/ 未就学児童 550円  ★山岳学舎ご宿泊者は1,000円 / 未就学児童 無料!!
【ムーンライトトレック】
■催行期間 2019年12月28日~2020年1月5日毎日
2,019年1月11日~3月22日までの土日祝祭日のみ  一日2回
■料  金 小学生以上3,800円(スノーシューレンタル料込)

<施設情報>くるみ原山岳学舎
宿泊 お一人様10,900円~(1泊2食)」〒503-2417 岐阜県大野郡白川村桐ヶ平518
05769-3-4072 https://kurumi-lodge.example.jp/ info@kurumi-gakusha.example

```html
<!DOCTYPE html>
<html lang="ja">
<head>
<meta charset="utf-8">
<title>冬の白川郷で遊ぼう!</title>
<link rel="stylesheet" href="https://fonts.googleapis.com/css2?family=Noto+Sans+JP:wght@400;500;700;900&family=Noto+Serif+JP:wght@700;900&display=swap">
<style>
:root{
  --navy:#0f1f4d;
  --navy-deep:#0a153a;
  --snow:#ffffff;
  --ice:#dfe8f6;
  --sky:#5d7fc2;
  --badge:#2a4a94;
  --ink:#1b2448;
  --accent:#e8f0ff;
}
*{margin:0;padding:0;box-sizing:border-box}
html,body{width:851px;height:1200px;overflow:hidden;background:var(--navy)}
.poster{position:relative;width:851px;height:1200px;overflow:hidden;background:var(--navy);font-family:"Noto Sans JP",sans-serif;color:var(--snow)}
.photo{position:absolute}
.hero-village{left:0;top:0;width:851px;height:380px;background:linear-gradient(180deg,#2b3f75 0%,#6d86bb 45%,#c9d6ec 70%,#0f1f4d 100%)}
.bottom-village{left:0;top:760px;width:851px;height:340px;background:linear-gradient(180deg,var(--navy) 0%,#2c467f 40%,#8aa2cf 70%,#3b5590 100%)}
.title{position:absolute;font-family:"Noto Serif JP",serif;font-weight:900;color:var(--snow);text-shadow:0 0 10px rgba(10,21,58,.6)}
.title-winter{left:360px;top:8px;font-size:96px;line-height:1}
.title-no{left:458px;top:56px;font-size:44px;line-height:1}
.title-col{writing-mode:vertical-rl;font-size:92px;line-height:1;letter-spacing:2px}
.title-col.place{left:338px;top:120px}
.title-col.play{left:436px;top:190px}
.title-col .small{font-size:60px}
.activity-photo{position:absolute;border-radius:50%;border:4px solid var(--snow);overflow:hidden}
.walk-photo{left:20px;top:150px;width:280px;height:230px;background:linear-gradient(160deg,#e9eef7 0%,#b9c7de 55%,#5b6f9c 100%)}
.trek-photo{left:555px;top:150px;width:280px;height:230px;background:linear-gradient(200deg,#f3f6fb 0%,#a9bfe2 50%,#3e5d9c 100%)}
.activity-label{position:absolute;background:var(--snow);color:var(--ink);font-family:"Noto Serif JP",serif;font-weight:700;text-align:center;border-radius:50% 50% 40% 40%;padding:14px 10px 10px}
.activity-label .sub{display:block;font-family:"Noto Sans JP",sans-serif;font-size:11px;font-weight:500;color:var(--badge)}
.walk-label{left:44px;top:112px;width:230px;font-size:24px}
.trek-label{left:574px;top:112px;width:250px;font-size:22px}
.activity-info{position:absolute;top:400px;width:285px}
.walk-info{left:24px}
.trek-info{left:546px}
.lead{font-size:10.5px;line-height:1.75;color:var(--ice);margin-bottom:12px}
.row{display:flex;align-items:flex-start;gap:10px;margin-bottom:10px}
.badge{flex:none;width:62px;height:62px;border-radius:50%;background:var(--badge);border:2px solid var(--sky);display:flex;align-items:center;justify-content:center;font-size:13px;font-weight:700}
.badge.period{border-radius:8px;height:26px;width:84px;margin:0 auto 6px}
.block{margin-bottom:12px;text-align:center}
.block p{font-size:12px;line-height:1.55}
.block .big{font-size:18px;font-weight:700}
.block .note{font-size:9.5px;color:var(--ice)}
.center-photo{left:320px;top:560px;width:210px;height:210px;border-radius:50%;border:4px solid var(--snow);background:radial-gradient(circle at 50% 40%,#f7c873 0%,#b86b3a 30%,#3a2a4a 70%,#141a3a 100%)}
.mini-photo{width:62px;height:62px;border-radius:50%;border:3px solid var(--snow)}
.mini-lantern{left:300px;top:700px;background:radial-gradient(circle,#ffd98a,#8a4a2a)}
.mini-slider{left:470px;top:735px;background:linear-gradient(135deg,#ffffff,#8fb0e0)}
.stay-box{position:absolute;left:470px;top:1010px;width:360px;height:76px;background:var(--snow);border-radius:14px;color:var(--ink);display:flex;align-items:center;padding:0 14px;gap:10px}
.stay-tag{flex:none;width:48px;height:48px;border-radius:50%;background:#c43a3a;color:var(--snow);font-size:15px;font-weight:700;display:flex;align-items:center;justify-content:center;writing-mode:vertical-rl}
.stay-price{font-size:15px;font-weight:700}
.stay-price strong{font-size:36px;font-weight:900;color:var(--navy)}
.stay-price small{font-size:11px}
.footer{position:absolute;left:0;top:1100px;width:851px;height:100px;background:var(--snow);color:var(--ink);display:flex;align-items:center;padding:0 24px;gap:20px}
.brand{display:flex;align-items:center;gap:10px}
.brand-mark{width:34px;height:34px;border-radius:50%;background:var(--navy)}
.brand-name{font-size:13px;font-weight:700;line-height:1.35}
.brand-name .ja{display:block;font-size:19px}
.contact{margin-left:auto;text-align:right}
.tel{display:flex;align-items:center;gap:8px;font-size:30px;font-weight:900;color:var(--navy);justify-content:flex-end}
.tel svg{width:28px;height:28px}
.contact-small{font-size:10px;line-height:1.5;color:#3a4670}
</style>
</head>
<body>
<div class="poster">
  <div class="photo hero-village" role="img" aria-label="雪に覆われた合掌造りの集落と山々の夜景"></div>
  <div class="photo bottom-village" role="img" aria-label="雪の夜にライトアップされた山岳学舎の建物"></div>

  <div class="title title-winter">冬</div>
  <div class="title title-no">の</div>
  <div class="title title-col place">白川郷</div>
  <div class="title title-col play"><span class="small">で</span>遊ぼう!</div>

  <div class="activity-photo walk-photo" role="img" aria-label="雪の森を歩く親子の写真"></div>
  <div class="activity-label walk-label"><span class="sub">はじめてのスノーシューに</span>星あかりの小径</div>
  <div class="activity-photo trek-photo" role="img" aria-label="スノーシューで雪山を歩く人の写真"></div>
  <div class="activity-label trek-label"><span class="sub">冬の野山をスノーシューで歩こう</span>ムーンライトトレック</div>

  <section class="activity-info walk-info">
    <p class="lead">雪に覆われた森の中をスノーシューで歩きます。動物の足跡や冬芽を探しながら、静かな冬の森を楽しみましょう。ご家族やはじめての方にもおすすめのやさしいコースです。</p>
    <div class="block">
      <div class="badge period">催行期間</div>
      <p>2019年12月14日(土)~<br>2020年4月5日(日) 一日3回</p>
    </div>
    <div class="block">
      <div class="badge period">料　金</div>
      <p>小学生以上 <span class="big">2,000円</span></p>
      <p>未就学児童 550円</p>
      <p class="note">★山岳学舎ご宿泊者は1,000円 / 未就学児童 無料!!</p>
    </div>
  </section>

  <section class="activity-info trek-info">
    <p class="lead">雪原や尾根をスノーシューで進み、冬の絶景を目指します。ふかふかの新雪を歩く楽しさと、山の上から見渡す白い世界をぜひ体験してください。体力に自信のある方に。</p>
    <div class="block">
      <div class="badge period">催行期間</div>
      <p>2019年12月28日~2020年1月5日 毎日<br>1月11日~3月22日の土日祝のみ 一日2回</p>
    </div>
    <div class="block">
      <div class="badge period">料　金</div>
      <p>小学生以上 <span class="big">3,800円</span></p>
      <p class="note">(スノーシューレンタル料込)</p>
    </div>
  </section>

  <div class="photo center-photo" role="img" aria-label="夜空に上がるスカイランタンの写真"></div>
  <div class="photo mini-photo mini-lantern" role="img" aria-label="スカイランタンの小さな丸写真"></div>
  <div class="photo mini-photo mini-slider" role="img" aria-label="スノースライダーの小さな丸写真"></div>

  <div class="stay-box">
    <div class="stay-tag">宿泊</div>
    <div class="stay-price">お一人様<strong>10,900</strong>円~<small>(1泊2食)</small></div>
  </div>

  <footer class="footer">
    <div class="brand">
      <div class="brand-mark"></div>
      <div class="brand-name">KURUMIHARA Mountain School<span class="ja">くるみ原山岳学舎</span></div>
    </div>
    <div class="contact">
      <div class="tel">
        <svg viewBox="0 0 24 24" aria-hidden="true"><path fill="#0f1f4d" d="M6.6 10.8a15.1 15.1 0 0 0 6.6 6.6l2.2-2.2c.3-.3.7-.4 1-.2 1.1.4 2.3.6 3.6.6.6 0 1 .4 1 1V20c0 .6-.4 1-1 1A17 17 0 0 1 3 4c0-.6.4-1 1-1h3.5c.6 0 1 .4 1 1 0 1.3.2 2.5.6 3.6.1.3 0 .7-.2 1z"/></svg>
        05769-3-4072
      </div>
      <p class="contact-small">〒503-2417 岐阜県大野郡白川村桐ヶ平518<br>https://kurumi-lodge.example.jp/　info@kurumi-gakusha.example</p>
    </div>
  </footer>
</div>
</body>
</html>
```